Moodvane - Landing Page

Need a landing page for a journal app. The app is based on a retrospective board, where each journal entry is split into 3 sections: "What went well", "What Didn't Go Well" and "Things To Try".
The landing page should match the style of all modern web application landing pages. Think Plumo, Vexora, Zenquil. I've included screenshots of the app.
One feature that I want to highlight that is not ready yet, is an AI coach. It will offer insights based on the history of the user's journal entries
1 page

```html
<!DOCTYPE html>
<html lang="en">
<head>
<meta charset="utf-8">
<title>Moodvane – Retrospective Journal</title>
<link href="https://fonts.googleapis.com/css2?family=Arimo:wght@400;700&family=Poppins:wght@400;500;600&display=swap" rel="stylesheet">
<style>
:root{
  --blue-deep:#0d3a74;
  --blue:#1c5aa3;
  --accent:#2b78c6;
  --accent-light:#4a90d9;
  --navy:#15233f;
  --ink:#1b2140;
  --text:#5f6675;
  --muted:#8a909c;
  --line:#e3e6ec;
  --grey-bg:#eef0f4;
  --white:#ffffff;
  --app-side:#1f2a36;
  --app-green:#5cc96a;
}
*{box-sizing:border-box;margin:0;padding:0}
html,body{width:1200px;height:4277px;overflow:hidden}
body{position:relative;background:var(--white);font-family:"Poppins",sans-serif;color:var(--ink)}
.abs{position:absolute}
h1,h2,h3,.brand{font-family:"Arimo",sans-serif}

/* Hero */
.hero{left:0;top:0;width:1200px;height:750px;background:
  radial-gradient(ellipse 520px 380px at 720px 330px,rgba(120,170,230,.35),transparent 70%),
  linear-gradient(180deg,#0c3670 0%,#154d92 55%,#1d5ea8 100%)}
.brand{font-weight:700;color:var(--white)}
.nav-logo{left:133px;top:24px;font-size:34px}
.nav{left:343px;top:35px;font-size:12.5px;color:var(--white);letter-spacing:.3px}
.nav span{position:absolute;white-space:nowrap}
.nav .active::after{content:"";position:absolute;left:0;top:24px;width:34px;height:2px;background:var(--white)}
.nav-cta{left:935px;top:26px;width:125px;height:37px;border:1.5px solid var(--white);border-radius:3px;color:var(--white);font-size:11.5px;font-weight:600;display:flex;align-items:center;justify-content:center;letter-spacing:.4px}
.hero-kicker{left:125px;top:230px;font-size:21px;color:var(--white);font-family:"Arimo",sans-serif}
.hero-title{left:127px;top:265px;font-size:47px;line-height:56px;color:var(--white);font-weight:700}
.hero-text{left:129px;top:395px;width:440px;font-family:"Arimo",sans-serif;font-size:17px;line-height:26px;color:#dfe8f6}
.btn-solid{background:var(--accent-light);color:var(--white);font-size:14.5px;font-weight:600;display:flex;align-items:center;justify-content:center}
.hero-btn{left:130px;top:477px;width:170px;height:46px}
.dots{left:143px;top:556px;display:flex;gap:4px;align-items:center}
.dots i{width:6px;height:6px;border-radius:50%;background:rgba(255,255,255,.55);display:block}
.dots i.ring{width:11px;height:11px;border:2px solid var(--white);background:transparent}
.dots i.on{background:var(--white)}

/* App mockup */
.app{position:absolute;width:980px;height:780px;transform-origin:0 0;background:var(--white);overflow:hidden;font-family:"Arimo",sans-serif;color:#2a2f3a}
.app-side{position:absolute;left:0;top:0;width:55px;height:100%;background:var(--app-side)}
.app-side i{position:absolute;left:18px;width:18px;height:16px;border:2px solid #c9d0d8;border-radius:2px}
.app-side .logo{top:14px;background:var(--app-green);border-color:var(--app-green)}
.app-side .user{bottom:16px;width:20px;height:20px;border-radius:50%;background:#8a94a0;border:none}
.app-title{position:absolute;left:95px;top:20px;font-size:22px;font-weight:700}
.app-date{position:absolute;left:95px;top:60px;font-size:15px;display:flex;align-items:center;gap:12px}
.badge{background:#2d3e57;color:var(--white);font-size:12px;padding:4px 12px;border-radius:12px}
.badge.green{background:#3cc36c}
.cols{position:absolute;left:150px;top:110px;display:flex;gap:50px}
.col{width:345px;height:620px;border:1px solid #e1e4e9;border-radius:4px;padding:12px 14px}
.col-head{font-size:15px;display:flex;align-items:center;gap:10px;height:30px}
.col-head svg{width:16px;height:16px}
.editor{margin-top:10px;border:1px solid #d4d8de;height:555px}
.toolbar{background:#f4f5f7;border-bottom:1px solid #d4d8de;padding:8px 10px;font-size:13px;line-height:20px;color:#444;height:64px}
.area{margin:10px;border:1px solid #d4d8de;height:460px;padding:14px 18px;font-size:14px;line-height:20px;color:#333}
.area ul{padding-left:14px}

/* Logos */
.partners-head{left:0;top:798px;width:1200px;text-align:center;font-family:"Arimo",sans-serif;font-size:17px;color:var(--blue);letter-spacing:.3px}
.partner{top:867px;font-family:"Poppins",sans-serif;font-weight:600;font-size:28px;color:#6b6f78;display:flex;align-items:center;gap:8px}
.partner b{width:16px;height:16px;background:#6b6f78;display:block}
.divider{left:200px;top:962px;width:800px;height:1px;background:var(--line)}

/* Section text */
.kicker{font-family:"Arimo",sans-serif;font-size:15px;color:var(--accent)}
.sec-title{font-weight:700;color:var(--ink)}
.para{font-family:"Arimo",sans-serif;font-size:15.5px;line-height:26.5px;color:var(--text)}
.btn-outline{border:2px solid var(--blue);color:var(--blue);font-size:14px;font-weight:600;display:flex;align-items:center;justify-content:center}

/* About */
.about-visual{left:116px;top:1035px;width:464px;height:355px;background:#d9e4f3;overflow:hidden}
.about-disc{left:130px;top:0;width:400px;height:355px;border-radius:0 200px 200px 0/0 180px 180px 0;background:var(--white)}
.list-app{left:185px;top:1075px;width:370px;height:275px;background:var(--white);box-shadow:0 0 0 1px #e6e9ee;overflow:hidden;font-family:"Arimo",sans-serif}
.list-app .side{position:absolute;left:0;top:0;width:17px;height:100%;background:var(--app-side)}
.list-app .add{position:absolute;left:58px;top:22px;font-size:5.5px;border:1px solid #ccd;padding:2px 5px;font-weight:700}
.entry-card{position:absolute;left:55px;width:300px;border:1px solid #e3e6eb;padding:6px 7px;font-size:5.2px;line-height:7.2px;color:#333}
.entry-card strong{font-size:6px;display:block;margin-bottom:2px}
.entry-card em{font-style:normal;color:#8a8f99;display:block}

/* Services */
.services{left:0;top:1497px;width:1200px;height:576px;background:var(--grey-bg)}
.svc-title{left:128px;top:1585px;font-size:31px;line-height:37px}
.svc-intro{left:455px;top:1590px;width:570px;font-family:"Arimo",sans-serif;font-size:14.5px;line-height:23px;color:var(--text)}
.card{background:var(--white)}
.card.dark{background:var(--navy);box-shadow:0 10px 30px rgba(20,35,63,.25)}
.card svg{position:absolute}
.card h3{position:absolute;font-size:17px;font-weight:600;font-family:"Arimo",sans-serif;color:var(--ink);white-space:nowrap}
.card p{position:absolute;font-family:"Arimo",sans-serif;font-size:10.8px;line-height:17px;color:var(--muted);width:235px}
.card .mini-btn{position:absolute;width:115px;height:32px;border:2px solid var(--blue);color:var(--blue);font-size:9px;font-weight:600;display:flex;align-items:center;justify-content:center}
.card.dark h3{color:var(--white)}
.card.dark p{color:#d8deea}
.card.dark .mini-btn{border-color:var(--white);color:var(--white)}

/* AI coach */
.ai{left:0;top:2073px;width:1200px;height:521px;background:linear-gradient(100deg,#1a2f6d 0%,#15346e 45%,#0d2f66 60%,#15407f 100%)}
.ai-visual{left:0;top:2073px;width:640px;height:521px;background:
  radial-gradient(circle 150px at 300px 210px,rgba(220,200,255,.75),rgba(90,140,240,.45) 55%,transparent 100%),
  radial-gradient(ellipse 380px 200px at 260px 430px,rgba(70,110,210,.55),transparent 75%),
  linear-gradient(90deg,#3a3f8f 0%,#2a3d88 60%,rgba(21,52,110,0) 100%)}
.ai-title{left:607px;top:2196px;font-size:44px;color:var(--white)}
.ai-text{left:610px;top:2261px;width:470px;font-family:"Arimo",sans-serif;font-size:15.5px;line-height:26.5px;color:#e2e9f5}
.ai-btn{left:611px;top:2392px;width:169px;height:46px}

/* Feature rows */
.feature-bg{left:0;top:2594px;width:1200px;height:1160px;background:linear-gradient(180deg,#ffffff 0%,#f6f8fb 60%,#eef2f8 100%)}
.blob{border-radius:50%;background:var(--blue)}
.screen-frame{border:2px solid #2a2d33;border-radius:8px;background:var(--white);overflow:hidden;box-shadow:0 10px 25px rgba(0,0,0,.12)}
.laptop{left:-30px;top:3205px;width:540px;height:395px;background:#1d1f24;border-radius:14px;overflow:hidden}
.laptop-screen{position:absolute;left:12px;top:12px;width:516px;height:378px;background:var(--white);overflow:hidden}
.laptop-base{left:-30px;top:3600px;width:605px;height:16px;background:linear-gradient(180deg,#d9dce1,#9aa0a8);border-radius:0 0 14px 14px}
.laptop-notch{left:155px;top:3600px;width:115px;height:7px;background:#8c9199;border-radius:0 0 6px 6px}

/* Newsletter & footer */
.footer-wave{left:0;top:3800px;width:1200px;height:477px}
.newsletter{left:138px;top:3752px;width:921px;height:160px;background:linear-gradient(90deg,#1b55a0,#2a74c3)}
.nl-title{left:192px;top:3790px;font-size:21px;line-height:29px;font-weight:600;color:var(--white);font-family:"Poppins",sans-serif}
.nl-sub{left:192px;top:3858px;font-size:12px;color:#dbe6f5}
.nl-input{left:525px;top:3812px;width:332px;height:42px;background:var(--white);font-size:10px;color:#8a8f99;padding-left:18px;display:flex;align-items:center}
.nl-btn{left:865px;top:3812px;width:139px;height:42px;background:var(--navy);color:var(--white);font-size:13px;font-weight:600;display:flex;align-items:center;justify-content:center}
.foot-logo{left:150px;top:3990px;font-size:32px}
.foot-about{left:150px;top:4040px;width:250px;font-size:11.5px;line-height:15px;color:#dbe4f2}
.foot-col{font-size:13px;color:#e3eaf5;line-height:31px}
.foot-col h4{font-size:14px;font-weight:500;color:var(--white);margin-bottom:2px;letter-spacing:.3px}
.social{top:4018px;width:27px;height:27px;border:1.5px solid var(--white);border-radius:50%}
.foot-bottom{top:4237px;font-size:10.5px;color:#dbe4f2}
</style>
</head>
<body>

<!-- Hero -->
<section class="abs hero"></section>
<div class="abs brand nav-logo">Moodvane</div>
<nav class="abs nav">
  <span class="active" style="left:0">HOME</span>
  <span style="left:82px">ABOUT</span>
  <span style="left:170px">SOLUTION</span>
  <span style="left:280px">RESOURCES</span>
  <span style="left:402px">PRICING</span>
  <span style="left:500px">CONTACT</span>
</nav>
<div class="abs nav-cta">GET STARTED</div>
<p class="abs hero-kicker">Welcome to Moodvane</p>
<h1 class="abs hero-title">Retrospective board<br>Applications</h1>
<p class="abs hero-text">Praesent vitae lacus Ut velit enim vestibulum non fer-<br>mentum nec hendrerit quis leo Pellentes</p>
<div class="abs btn-solid hero-btn">LEARN MORE</div>
<div class="abs dots"><i class="ring"></i><i class="on"></i><i></i><i></i><i></i><i class="ring"></i></div>

<div class="app" style="left:612px;top:148px;transform:scale(.6);width:980px;height:795px">
  <aside class="app-side"><i class="logo"></i><i style="top:60px"></i><i style="top:90px"></i><i style="top:120px"></i><i class="user"></i></aside>
  <div class="app-title">Entry</div>
  <div class="app-date">▦ Wed Aug 21 2024 ⌄ <span class="badge">Default Journal</span></div>
  <div class="cols">
    <div class="col"><div class="col-head"><svg viewBox="0 0 16 16"><rect x="1" y="7" width="4" height="8" fill="#3b7bd1"/><path d="M6 7l4-6 2 1-1 5h4v8H6z" fill="#3b7bd1"/></svg>What Went Well?</div>
      <div class="editor"><div class="toolbar">Normal ⇕ &nbsp; <b>B</b> <i>I</i> <u>U</u> S ”<br>≡ ≡ ≡ ≡ &nbsp;T</div><div class="area"></div></div></div>
    <div class="col"><div class="col-head"><svg viewBox="0 0 16 16"><path d="M8 1l7 14H1z" fill="#3b7bd1"/></svg>What Didn't Go Well?</div>
      <div class="editor"><div class="toolbar">Normal ⇕ &nbsp; <b>B</b> <i>I</i> <u>U</u> S ”<br>≡ ≡ ≡ ≡ &nbsp;T</div><div class="area"></div></div></div>
    <div class="col"><div class="col-head">Things To Try</div>
      <div class="editor"><div class="toolbar">Normal</div><div class="area"></div></div></div>
  </div>
</div>

<!-- Partners -->
<p class="abs partners-head">JOINED COMPANIES USING OUR PLATFORM</p>
<div class="abs partner" style="left:115px"><b></b>Tilevo</div>
<div class="abs partner" style="left:340px;font-size:22px"><b style="border-radius:50%"></b>Unified Waters</div>
<div class="abs partner" style="left:555px">Railcor</div>
<div class="abs partner" style="left:770px">Studunion</div>
<div class="abs partner" style="left:995px">Cardwise</div>
<div class="abs divider"></div>

<!-- About -->
<div class="abs about-visual"><div class="abs about-disc"></div></div>
<div class="abs list-app">
  <div class="side"></div>
  <div class="add">+ Add New</div>
  <div class="entry-card" style="top:50px;height:130px">
    <strong>Thu Aug 22 2024</strong><em>What Went Well</em>
    Completed all planned workouts this week.<br>Raised bench press weight by 10 pounds.<br>Kept steady energy through sessions.<br><em>What Didn't Go Well</em>Skipped two stretching sessions.<br><em>Things To Try</em>Focus on form next week.
  </div>
  <div class="entry-card" style="top:235px;height:60px">
    <strong>Tue Aug 20 2024</strong><em>What Went Well</em>Reached a personal best in squats.
  </div>
</div>
<p class="abs kicker" style="left:652px;top:1045px">Lorem ipsum dolor sit ame</p>
<h2 class="abs sec-title" style="left:651px;top:1072px;font-size:44px">About Moodvane</h2>
<p class="abs para" style="left:652px;top:1143px;width:460px">Lorem ipsum dolor sit amet, consectetur adipiscing elit, sed do eiusmod tempor incididunt ut labore et dolore magna aliqua. Ut enim ad minim veniam, quis nostrud exercitation ullamco laboris nisi ut aliquip ex ea commodo consequat. Duis aute irure dolor in reprehenderit in voluptate velit esse cillum dolore eu fugiat nulla pariatur. Excepteur sint occaecat</p>
<div class="abs btn-outline" style="left:653px;top:1333px;width:163px;height:47px">LEARN MORE</div>

<!-- Services -->
<section class="abs services"></section>
<h2 class="abs sec-title svc-title">Service Delivering<br>Solutions</h2>
<p class="abs svc-intro">Praesent vitae lacus Ut velit enim vestibulum non fermentum nec hendrerit quis leo Pellentesque rutrum malesuada neque Nunc tempus felis vitae</p>

<div class="abs card" style="left:125px;top:1713px;width:302px;height:250px">
  <svg style="left:42px;top:30px" width="42" height="36" viewBox="0 0 42 36" fill="none" stroke="#3b7bd1" stroke-width="1.6"><rect x="2" y="2" width="38" height="26"/><path d="M14 34h14M21 28v6M11 22v-6M17 22v-10M23 22v-7M29 22v-12"/></svg>
  <h3 style="left:35px;top:85px">Sed ut perspiciatis</h3>
  <p style="left:35px;top:118px">Praesent vitae lacus Ut velit enim vestibulum non fermentum nec hendrerit quis leo Pellentesque rutrum malesuada neque</p>
  <div class="mini-btn" style="left:35px;top:190px">LEARN MORE</div>
</div>
<div class="abs card dark" style="left:443px;top:1686px;width:302px;height:295px">
  <svg style="left:33px;top:35px" width="60" height="60" viewBox="0 0 60 60" fill="none" stroke="#8fb2e6" stroke-width="1.6"><circle cx="14" cy="16" r="8"/><circle cx="14" cy="16" r="3"/><circle cx="46" cy="14" r="7"/><circle cx="44" cy="44" r="10"/><path d="M39 44l4 4 7-8M14 24v20h20M22 16h17"/></svg>
  <h3 style="left:32px;top:112px">Neque porro quisquam</h3>
  <p style="left:35px;top:145px">Praesent vitae lacus Ut velit enim vestibu-lum non fermentum nec hendrerit quis leo Pellentesque rutrum malesuada neque</p>
  <div class="mini-btn" style="left:35px;top:217px">LEARN MORE</div>
</div>
<div class="abs card" style="left:761px;top:1713px;width:302px;height:250px">
  <svg style="left:40px;top:28px" width="48" height="40" viewBox="0 0 48 40" fill="none" stroke="#3b7bd1" stroke-width="1.6"><rect x="2" y="2" width="44" height="28"/><path d="M18 38h12M24 30v8"/><rect x="8" y="8" width="6" height="5"/><rect x="8" y="17" width="6" height="5"/><path d="M18 11h14M18 20h14"/></svg>
  <h3 style="left:40px;top:85px">Auis nostrum exercitati</h3>
  <p style="left:40px;top:118px">Praesent vitae lacus Ut velit enim vestibulum non fermentum nec hendrerit quis leo Pellentesque rutrum malesuada neque</p>
  <div class="mini-btn" style="left:40px;top:190px">LEARN MORE</div>
</div>

<!-- AI coach -->
<section class="abs ai"></section>
<div class="abs ai-visual" role="img" aria-label="Glowing digital brain resting on a circuit board"></div>
<h2 class="abs ai-title">AI Coach</h2>
<p class="abs ai-text">Lorem ipsum dolor sit amet, consectetur adipiscing elit, sed do eiusmod tempor incididunt ut labore et dolore magna aliqua. Ut enim ad minim veniam, quis nostrud exercitation ullamco laboris nisi ut aliquip ex ea commodo conseq</p>
<div class="abs btn-solid ai-btn">LEARN MORE</div>

<!-- Feature rows -->
<div class="abs feature-bg"></div>
<p class="abs kicker" style="left:119px;top:2703px">Lorem ipsum dolor sit ame</p>
<h2 class="abs sec-title" style="left:120px;top:2737px;font-size:27px;line-height:27px">Quis autem vel eum iure repre-<br>henderit qui in ea voluptate</h2>
<p class="abs para" style="left:120px;top:2813px;width:460px">Lorem ipsum dolor sit amet, consectetur adipiscing elit, sed do eiusmod tempor incididunt ut labore et dolore magna aliqua. Ut enim ad minim veniam, quis nostrud exercitation ullamco laboris nisi ut aliquip ex ea commodo consequat. Duis aute irure dolor in reprehenderit in voluptate velit esse</p>
<div class="abs btn-outline" style="left:120px;top:2978px;width:163px;height:47px">LEARN MORE</div>

<div class="abs blob" style="left:990px;top:2655px;width:150px;height:150px"></div>
<div class="abs screen-frame" style="left:627px;top:2697px;width:473px;height:355px">
  <div class="app" style="left:0;top:0;transform:scale(.483)">
    <aside class="app-side"><i class="logo"></i><i style="top:60px"></i><i style="top:90px"></i><i style="top:120px"></i><i class="user"></i></aside>
    <div class="app-title">Entry</div>
    <div class="app-date">▦ Thu Aug 22 2024 ⌄ <span class="badge green">Gym</span></div>
    <div class="cols">
      <div class="col"><div class="col-head"><svg viewBox="0 0 16 16"><rect x="1" y="7" width="4" height="8" fill="#3b7bd1"/><path d="M6 7l4-6 2 1-1 5h4v8H6z" fill="#3b7bd1"/></svg>What Went Well?</div>
        <div class="editor"><div class="toolbar">Normal ⇕ &nbsp; <b>B</b> <i>I</i> <u>U</u> S ”<br>≡ ≡ ≡ ≡ &nbsp;T</div><div class="area"><ul><li>Completed all planned workouts this week.</li><li>Increased bench press by 10 pounds.</li><li>Kept energy steady in sessions.</li></ul></div></div></div>
      <div class="col"><div class="col-head"><svg viewBox="0 0 16 16"><path d="M8 1l7 14H1z" fill="#3b7bd1"/></svg>What Didn't Go Well?</div>
        <div class="editor"><div class="toolbar">Normal ⇕ &nbsp; <b>B</b> <i>I</i> <u>U</u> S ”<br>≡ ≡ ≡ ≡ &nbsp;T</div><div class="area"><ul><li>Struggled with form on deadlifts.</li><li>Missed two stretching sessions.</li><li>Skipped meal prep this week.</li></ul></div></div></div>
      <div class="col"><div class="col-head">Things To Try</div>
        <div class="editor"><div class="toolbar">Normal ⇕</div><div class="area"><ul><li>Focus on form</li><li>Add stretching</li></ul></div></div></div>
    </div>
  </div>
</div>

<div class="abs blob" style="left:405px;top:3495px;width:150px;height:150px"></div>
<div class="abs laptop">
  <div class="laptop-screen">
    <div class="app" style="left:-28px;top:0;transform:scale(.53)">
      <aside class="app-side"></aside>
      <div class="app-title">Entry</div>
      <div class="app-date">▦ Wed Aug 21 2024 ⌄ <span class="badge">Default Journal</span></div>
      <div class="cols" style="left:95px">
        <div class="col"><div class="col-head"><svg viewBox="0 0 16 16"><rect x="1" y="7" width="4" height="8" fill="#3b7bd1"/><path d="M6 7l4-6 2 1-1 5h4v8H6z" fill="#3b7bd1"/></svg>What Went Well?</div>
          <div class="editor"><div class="toolbar">Normal ⇕ &nbsp; <b>B</b> <i>I</i> <u>U</u> S ”<br>≡ ≡ ≡ ≡ &nbsp;T</div><div class="area"></div></div></div>
        <div class="col"><div class="col-head"><svg viewBox="0 0 16 16"><path d="M8 1l7 14H1z" fill="#3b7bd1"/></svg>What Didn't Go Well?</div>
          <div class="editor"><div class="toolbar">Normal ⇕ &nbsp; <b>B</b> <i>I</i> <u>U</u> S ”<br>≡ ≡ ≡ ≡ &nbsp;T</div><div class="area"></div></div></div>
        <div class="col"><div class="col-head"><svg viewBox="0 0 16 16"><circle cx="8" cy="8" r="6" fill="#3b7bd1"/></svg>Things To Try</div>
          <div class="editor"><div class="toolbar">Normal ⇕ &nbsp; <b>B</b> <i>I</i> <u>U</u> S ”<br>≡ ≡ ≡ ≡ &nbsp;T</div><div class="area"></div></div></div>
      </div>
    </div>
  </div>
</div>
<div class="abs laptop-base"></div>
<div class="abs laptop-notch"></div>

<p class="abs kicker" style="left:620px;top:3268px">Lorem ipsum dolor sit ame</p>
<h2 class="abs sec-title" style="left:622px;top:3303px;font-size:27px;line-height:27px">Sed ut perspiciatis unde omnis<br>iste natus error sit</h2>
<p class="abs para" style="left:622px;top:3383px;width:460px">Lorem ipsum dolor sit amet, consectetur adipiscing elit, sed do eiusmod tempor incididunt ut labore et dolore magna aliqua. Ut enim ad minim veniam, quis nostrud exercitation ullamco laboris nisi ut aliquip ex ea commodo consequat. Duis aute irure dolor in reprehenderit in voluptate velit esse</p>
<div class="abs btn-outline" style="left:624px;top:3545px;width:163px;height:47px">LEARN MORE</div>

<!-- Footer -->
<svg class="abs footer-wave" viewBox="0 0 1200 477" preserveAspectRatio="none">
  <defs><linearGradient id="footGrad" x1="0" y1="0" x2="0" y2="1"><stop offset="0" stop-color="#123f80"/><stop offset="1" stop-color="#0c2f66"/></linearGradient></defs>
  <path d="M0 70 C150 20 260 110 420 60 C600 5 780 90 960 40 C1080 10 1150 40 1200 30 L1200 477 L0 477Z" fill="url(#footGrad)"/>
</svg>
<div class="abs newsletter"></div>
<p class="abs nl-title">Subscribe to Our Newsletter<br>for latest updates</p>
<p class="abs nl-sub">Sed ut perspiciatis unde omnis</p>
<div class="abs nl-input">Your Email address</div>
<div class="abs nl-btn">SUBSCRIBE</div>

<div class="abs brand foot-logo">Moodvane</div>
<p class="abs foot-about">malesuada neque Nunc tempus felis vitae urna Vivamus porttitor neque at volutpat rutrum purus nisi eleifend libero a</p>
<div class="abs foot-col" style="left:435px;top:3980px"><h4>COMPANY</h4>About<br>Career<br>Blogs<br>Technology<br>Products</div>
<div class="abs foot-col" style="left:597px;top:3980px"><h4>LINKS</h4>Support<br>FAQ<br>Press<br>News<br>Blogs</div>
<div class="abs foot-col" style="left:763px;top:3980px;line-height:30px"><h4>RESOURCES</h4>Help Desk<br>Pricing<br>Security<br>Clients<br>Open Source</div>
<div class="abs foot-col" style="left:922px;top:3978px"><h4>FOLLOW US</h4></div>
<div class="abs social" style="left:925px"></div>
<div class="abs social" style="left:960px"></div>
<div class="abs social" style="left:995px"></div>
<div class="abs social" style="left:1030px"></div>
<p class="abs foot-bottom" style="left:168px">© 2024 Moodvane | All Rights Reserved</p>
<p class="abs foot-bottom" style="left:907px">Term of Use | Privacy Policy</p>

</body>
</html>
```